New Digital Marketing Company Needs Web Design

Introduction

Pixelbrook gives advice to small businesses about their websites and digital marketing strategies and builds working relationships with clients to understand their business and maximise its online presence.

Pixelbrook offers services to support its clients needs such as: website auditing & search engine optimisation (SEO), Zorvani Promoline, Chatterloop advertising, newsletter development & management, online performance reporting, email setup & management, website hosting, maintenance & backup, web development, web updates & web design.

Design Specification

The site should have a clean & professional look and use the colour scheme from the logo (attached below).

The design should consist of 2 templates; The homepage & content page.

Homepage Design

The homepage should have a header with logo, contact number and email and menu. Followed underneath by a slider and then individual blocks for key services. Under the key services should be a testimonial block with 3 testimonials. Finally the footer with company details, menu links and location map.

Header Info:

Contact number: 01632 960418
Email: info@pixelbrook.co.uk

Menu: Home Services About Contact

Slider Design:

The slider should be full page and show an image with text.

Key Services:

The key services should have a relevant icon and brief description.

The key services are:

Digital Marketing

Website Hosting & Management

Website Health Check (SEO)

Website Updating & Development

Newsletter Management

Email Management

Note: Lorem Ipsum can be used for brief description...

Testimonials:

There should be 3 testimonials side by side and they should include a headshot image of the person giving the testimonial.

Note: Lorem Ipsum and sample images can be used for testimonials...

Footer:

The footer should have 3 sections:

Menu links:

Digital Marketing About
Zorvani Promoline Contact
Chatterloop Advertising Privacy Policy
Search Engine Optimisation (SEO) Terms & Conditions
Website Hosting FAQ
Newsletter Management

Company Information:

PixelBrook
14 Farrow Close
Bracknell
Berskhire
ZX47 3LT
Tel: 01632 960418

Chatterloop icon - Quillo icon - Guildnet icon

Location

Zorvani map

Footer Bottom:

Copyright message.

Content Design

The content design should have the common header and footer.

Each content page should have a banner for image with text description (page title).

The content page should have area for text description and area for a video display if available.

There should be a right column (possibly) for modules (latest blog, latest Chatterloop feeds, testimonial)
Updates

Reason: I have had to extend the deadline as could not review while on vacation and need to feedback to some designers for content page design. Many thanks for your understanding.

Target Market(s)

Industry/Entity Type

Digital

Number of Pages Required

2 page

Requirements
Must have
• The site should have a clean & professional look and use the colour scheme from the logo (attached below).
• The design should consist of 2 templates; The homepage & content page.

```html
<!DOCTYPE html>
<html lang="en">
<head>
<meta charset="utf-8">
<title>PixelBrook – Web Design</title>
<link rel="stylesheet" href="https://fonts.googleapis.com/css2?family=Open+Sans:wght@400;600;700&display=swap">
<style>
:root{
  --navy:#2e2c55;
  --plum:#5b1f4f;
  --ink:#333333;
  --body:#5e5e5e;
  --muted:#8a8a8a;
  --line:#e6e6e6;
  --link:#2a6fd6;
  --white:#ffffff;
  --map:#e2e2e2;
  --pin:#d9443a;
}
*{box-sizing:border-box;margin:0;padding:0}
html,body{width:704px;height:1200px;overflow:hidden;background:var(--white)}
body{position:relative;font-family:"Open Sans",Arial,sans-serif;color:var(--body);-webkit-font-smoothing:antialiased}
.abs{position:absolute}
/* header */
.header{left:0;top:0;width:704px;height:56px;border-bottom:1px solid var(--line)}
.brand{left:84px;top:14px;display:flex;align-items:center;gap:6px}
.brand-dot{width:18px;height:18px;border-radius:50%;background:var(--plum)}
.brand-name{font-size:19px;font-weight:700;color:var(--plum);letter-spacing:-.2px}
.divider-v{top:0;width:1px;height:55px;background:var(--line)}
.contact-item{top:19px;display:flex;gap:8px;align-items:flex-start}
.contact-label{font-size:7px;color:var(--body);line-height:9px}
.contact-value{font-size:9px;font-weight:600;color:var(--plum);line-height:13px}
.nav{left:0;top:56px;width:704px;height:27px}
.nav a{position:absolute;top:9px;font-size:7.5px;letter-spacing:.6px;color:var(--ink);text-decoration:none}
.nav .active-bar{top:-1px;left:137px;width:61px;height:2px;background:var(--navy)}
/* banner */
.banner{left:0;top:83px;width:704px;height:141px;background:linear-gradient(100deg,#7a5a3c 0%,#a37a52 35%,#8d6846 60%,#5a3a26 100%)}
.banner-title{left:0;top:141px;width:704px;text-align:center;font-size:15px;color:var(--white);letter-spacing:.3px}
/* main */
.page-title{left:84px;top:258px;font-size:15px;font-weight:600;color:var(--navy);letter-spacing:.5px}
.copy{left:84px;width:336px;font-size:6.8px;line-height:11.3px;color:var(--body)}
.photo{left:85px;top:526px;width:334px;height:175px;background:radial-gradient(ellipse at 55% 55%,#c9c9c4 0%,#6e5744 45%,#3a2a20 100%)}
/* sidebar */
.rule{left:450px;width:169px;height:2px;background:var(--navy)}
.side-title{left:450px;font-size:15px;font-weight:400;color:var(--navy)}
.blog-item{left:450px;width:169px;display:flex;gap:5px}
.blog-thumb{width:46px;height:46px;flex:none}
.blog-head{font-size:6.6px;font-weight:600;color:var(--ink);line-height:10px}
.blog-text{font-size:6px;line-height:9.3px;color:var(--body)}
.blog-more{font-size:6px;color:var(--link);line-height:9px}
.feed-item{left:450px;width:169px}
.feed-head{font-size:6.6px;font-weight:600;color:var(--ink)}
.feed-meta{margin-top:4px;font-size:6px;color:var(--muted);display:flex;align-items:center;gap:5px}
.feed-meta b{color:var(--body);font-weight:600}
/* footer */
.footer-rule{left:84px;top:797px;width:535px;height:2px;background:var(--line)}
.footer-title{top:833px;font-size:14px;font-weight:700;color:var(--ink);letter-spacing:.6px}
.footer-text{font-size:6.8px;line-height:11.2px;color:var(--ink)}
.footer-list{list-style:none;font-size:6.8px;line-height:11.2px;color:var(--ink)}
.footer-list li::before{content:"›";margin-right:5px}
.social{left:84px;top:904px;display:flex;gap:8px;font-size:6.5px;font-weight:600;color:var(--navy)}
.social-rule{left:84px;top:896px;width:138px;height:1px;background:var(--line)}
.news-field{left:450px;top:886px;width:137px;height:15px;border-bottom:1px solid var(--plum);font-size:5.6px;font-style:italic;color:var(--muted);padding-top:3px}
.map{left:0;top:959px;width:704px;height:211px;background:var(--map)}
.map-pin{left:338px;top:1058px}
.bottom-bar{left:84px;top:1181px;width:535px;display:flex;justify-content:space-between;font-size:6.8px;color:var(--muted)}
.bottom-links{display:flex;gap:15px;color:var(--ink)}
</style>
</head>
<body>
<header class="abs header">
  <div class="abs brand"><span class="brand-dot"></span><span class="brand-name">PixelBrook</span></div>
  <span class="abs divider-v" style="left:367px"></span>
  <div class="abs contact-item" style="left:379px">
    <svg width="10" height="10" viewBox="0 0 24 24" style="margin-top:4px"><path fill="#999" d="M6.6 10.8a15.1 15.1 0 006.6 6.6l2.2-2.2c.3-.3.7-.4 1-.2 1.1.4 2.3.6 3.6.6.6 0 1 .4 1 1V20c0 .6-.4 1-1 1A17 17 0 013 4c0-.6.4-1 1-1h3.5c.6 0 1 .4 1 1 0 1.3.2 2.5.6 3.6.1.3 0 .7-.2 1z"/></svg>
    <div><div class="contact-label">Contact us</div><div class="contact-value">01632 960418</div></div>
  </div>
  <span class="abs divider-v" style="left:471px"></span>
  <div class="abs contact-item" style="left:486px">
    <svg width="13" height="10" viewBox="0 0 26 18" style="margin-top:4px"><rect x="1" y="1" width="24" height="16" fill="none" stroke="#999" stroke-width="2"/><path d="M1 1l12 9 12-9" fill="none" stroke="#999" stroke-width="2"/></svg>
    <div><div class="contact-label">Email</div><div class="contact-value">info@pixelbrook.co.uk</div></div>
  </div>
  <span class="abs divider-v" style="left:631px"></span>
</header>
<nav class="abs nav">
  <span class="abs active-bar"></span>
  <a style="left:95px">HOME</a>
  <a style="left:147px">SERVICES</a>
  <a style="left:212px">ABOUT</a>
  <a style="left:268px">CONTACT</a>
</nav>

<div class="abs banner" role="img" aria-label="Desk scene with glasses, coffee mug and a web design notebook"></div>
<div class="abs banner-title">Service / Web Design</div>

<main>
  <h1 class="abs page-title">WEB DESIGN</h1>
  <p class="abs copy" style="top:288px">It is a long established fact that a reader will be distracted by the readable content of a page when looking at its layout. The point of using Lorem Ipsum is that it has a more-or-less normal distribution of letters, as opposed to using 'Content here, content here', making it look like readable English. Many desktop<br>publishing packages and web page editors now use Lorem Ipsum as their default model text, and a search for 'lorem ipsum' will uncover many web sites still in their infancy. Various versions have evolved over the years, sometimes by accident, sometimes on purpose (injected humour and the like).</p>
  <p class="abs copy" style="top:377px">Contrary to popular belief, Lorem Ipsum is not simply random text. It has roots in a piece of classical Latin literature from 45 BC, making it over 2000 years old. Edwin Harrow, a Latin professor at Larchmont College in Westmere, looked up one of the more obscure Latin words, consectetur, from a Lorem Ipsum passage, and going through the cites of the word in classical literature, discovered the undoubtable source. Lorem Ipsum comes from sections 1.10.32 and 1.10.33 of "de Finibus Bonorum et Malorum" (The Extremes of Good and Evil) by Aurelian Pell, written in 45 BC. This book is a treatise on the theory of ethics, very popular during the Renaissance. The first line of Lorem Ipsum, "Lorem ipsum dolor sit amet..", comes from a line in section 1.10.32.</p>
  <p class="abs copy" style="top:478px">The standard chunk of Lorem Ipsum used since the 1500s is reproduced below for those interested. Sections 1.10.32 and 1.10.33 from "de Finibus Bonorum et Malorum" by Aurelian Pell are also reproduced in their exact original form, accompanied by English versions from the 1914 translation by H. Tolland.</p>
  <div class="abs photo" role="img" aria-label="Laptop showing a website on a wooden table"></div>
  <p class="abs copy" style="top:717px">There are many variations of passages of Lorem Ipsum available, but the majority have suffered alteration in some form, by injected humour, or randomised words which don't look even slightly believable. If you are going to use a passage of Lorem Ipsum, you need to be sure there isn't anything embarrassing hidden in the middle of text.</p>
</main>

<aside>
  <span class="abs rule" style="top:261px"></span>
  <h2 class="abs side-title" style="top:268px">Latest blog</h2>
  <div class="abs blog-item" style="top:303px">
    <div class="blog-thumb" role="img" aria-label="Colourful icon blocks" style="background:linear-gradient(135deg,#d33 0%,#f0a020 50%,#2a8a3a 100%)"></div>
    <div><div class="blog-head">The best of themes website 2016</div><div class="blog-text">Lorem Ipsum is simply dummy text of the printing and typesetting industry</div><div class="blog-more">See more</div></div>
  </div>
  <div class="abs blog-item" style="top:363px">
    <div class="blog-thumb" role="img" aria-label="Hand touching web screens" style="background:linear-gradient(135deg,#2c5c9a,#9cc0e0 60%,#e8eef4)"></div>
    <div><div class="blog-head">How to web design?</div><div class="blog-text">Lorem Ipsum is simply dummy text of the printing and typesetting industry</div><div class="blog-more">See more</div></div>
  </div>
  <div class="abs blog-item" style="top:424px">
    <div class="blog-thumb" role="img" aria-label="Responsive website on several devices" style="background:linear-gradient(180deg,#f4f4f4,#bcc4cc 60%,#40464c)"></div>
    <div><div class="blog-head">Responsive for website.</div><div class="blog-text">Lorem Ipsum is simply dummy text of the printing and typesetting industry</div><div class="blog-more">See more</div></div>
  </div>

  <span class="abs rule" style="top:496px"></span>
  <h2 class="abs side-title" style="top:503px">Latest Chatterloop</h2>
  <div class="abs feed-item" style="top:535px"><div class="feed-head">The best of themes website 2016</div><div class="feed-meta"><svg width="6" height="6" viewBox="0 0 10 10"><circle cx="5" cy="5" r="4" fill="none" stroke="#999" stroke-width="1.3"/><path d="M5 2.5V5h2" fill="none" stroke="#999" stroke-width="1.2"/></svg><span>15/9/2016 by <b>Sam Porter</b></span></div></div>
  <div class="abs feed-item" style="top:573px"><div class="feed-head">Creative Ideas in banner for website</div><div class="feed-meta"><svg width="6" height="6" viewBox="0 0 10 10"><circle cx="5" cy="5" r="4" fill="none" stroke="#999" stroke-width="1.3"/><path d="M5 2.5V5h2" fill="none" stroke="#999" stroke-width="1.2"/></svg><span>15/9/2016 by <b>Sam Porter</b></span></div></div>
  <div class="abs feed-item" style="top:612px"><div class="feed-head">Learn more Html, Css</div><div class="feed-meta"><svg width="6" height="6" viewBox="0 0 10 10"><circle cx="5" cy="5" r="4" fill="none" stroke="#999" stroke-width="1.3"/><path d="M5 2.5V5h2" fill="none" stroke="#999" stroke-width="1.2"/></svg><span>15/9/2016 by <b>Sam Porter</b></span></div></div>
  <div class="abs feed-item" style="top:650px"><div class="feed-head">New Design</div><div class="feed-meta"><svg width="6" height="6" viewBox="0 0 10 10"><circle cx="5" cy="5" r="4" fill="none" stroke="#999" stroke-width="1.3"/><path d="M5 2.5V5h2" fill="none" stroke="#999" stroke-width="1.2"/></svg><span>15/9/2016 by <b>Sam Porter</b></span></div></div>
  <div class="abs feed-item" style="top:690px"><div class="feed-head">Digital Marketing &amp; Development Website</div><div class="feed-meta"><svg width="6" height="6" viewBox="0 0 10 10"><circle cx="5" cy="5" r="4" fill="none" stroke="#999" stroke-width="1.3"/><path d="M5 2.5V5h2" fill="none" stroke="#999" stroke-width="1.2"/></svg><span>15/9/2016 by <b>Sam Porter</b></span></div></div>
</aside>

<footer>
  <span class="abs footer-rule"></span>
  <h3 class="abs footer-title" style="left:84px">PIXELBROOK</h3>
  <div class="abs footer-text" style="left:84px;top:857px;width:140px">
    <div style="display:flex;gap:6px"><svg width="6" height="8" viewBox="0 0 10 14" style="margin-top:2px;flex:none"><path d="M5 0a5 5 0 00-5 5c0 4 5 9 5 9s5-5 5-9a5 5 0 00-5-5zm0 7a2 2 0 110-4 2 2 0 010 4z" fill="#333"/></svg><span>14 Farrow Close - Bracknell - Berskhire - ZX47 3LT</span></div>
    <div style="display:flex;gap:6px"><svg width="7" height="7" viewBox="0 0 24 24" style="margin-top:2px;flex:none"><path fill="#333" d="M6.6 10.8a15.1 15.1 0 006.6 6.6l2.2-2.2c.3-.3.7-.4 1-.2 1.1.4 2.3.6 3.6.6.6 0 1 .4 1 1V20c0 .6-.4 1-1 1A17 17 0 013 4c0-.6.4-1 1-1h3.5c.6 0 1 .4 1 1 0 1.3.2 2.5.6 3.6.1.3 0 .7-.2 1z"/></svg><span>Tel: 01632 960418</span></div>
  </div>
  <span class="abs social-rule"></span>
  <div class="abs social"><span>Chatterloop</span><span>Quillo</span><span>Guildnet</span></div>

  <h3 class="abs footer-title" style="left:268px">OUR SERVICE</h3>
  <ul class="abs footer-list" style="left:268px;top:857px">
    <li>Digital Marketing</li>
    <li>Zorvani Promoline</li>
    <li>Chatterloop Advertising</li>
    <li>Search Engine Optimisation (SEO)</li>
    <li>Website Hosting</li>
    <li>Newsletter Management</li>
  </ul>

  <h3 class="abs footer-title" style="left:450px">NEWSLETTER</h3>
  <p class="abs footer-text" style="left:450px;top:857px;width:130px">Don't miss to subscribe to our news feeds, kindly fill the form below.</p>
  <div class="abs news-field">You email Address</div>
  <svg class="abs" style="left:577px;top:890px" width="7" height="7" viewBox="0 0 10 10"><path d="M1 5h7M5 2l3 3-3 3" fill="none" stroke="#5b1f4f" stroke-width="1.6"/></svg>

  <div class="abs map" role="img" aria-label="Street map of the area around the office"></div>
  <svg class="abs map-pin" width="24" height="34" viewBox="0 0 24 34" aria-hidden="true"><path d="M12 1.5A10.5 10.5 0 001.5 12c0 8 10.5 20 10.5 20s10.5-12 10.5-20A10.5 10.5 0 0012 1.5z" fill="#fff" fill-opacity=".6" stroke="#d9443a" stroke-width="1.6"/><circle cx="12" cy="12" r="3.2" fill="#d9443a"/></svg>

  <div class="abs bottom-bar">
    <span>Copyright © 2016 Pixelbrook.</span>
    <span class="bottom-links"><span>About</span><span>Contact</span><span>Privacy Policy</span><span>Terms &amp; Conditions</span><span>FAQ</span></span>
  </div>
</footer>
</body>
</html>
```